お店の看板デザインを依頼させて頂きます。
看板は国道沿いに2つ、裏通りに1つ、スタンド看板1つを設置予定です。
スクールと共にサロン・ショップも展開している事が分かり、印象に残る様なデザインを希望します。
宜しくお願いいたします。
記載項目:電話番号 ・ロゴ・URL
ロゴはこちらのサイトで依頼、選定済(添付いたします)
URL 後日取得予定
看板は南北に走る国道に、北向きと西向きに一枚ずつ、裏通り東向きに一枚、スタンド看板の設置場所はお店の前か、国道から見える位置に置く予定です。

看板サイズ:国道沿い   H 2000 x W 1000 / H 2440 x W 1220
裏通り    H 910 x W 1820
スタンド看板 H 1300 x W 600
清潔、エレガント、高級なイメージを考えています
• 高解像度JPG (.jpg)
• イラストレーター形式 (.ai)
• フォトショップ形式 (.psd)
看板のデザインは縦型のもの1点でお願いします。
色はえんじ色でお願いします。

アロマテラピー(Aromatherapy)の文字を入れて頂き
アロマスクール(Aroma School)
ボディ&フェイシャル サロン(Body&Facial Salon)
アロマショップ(Aroma shop)
と入れて頂きたいです。
文字は英語でもカタカナでも両方使って頂いても構いません。

どうぞ宜しくお願いします。
たくさんのご提案ありがとうございます。

デザインの色ですが、えんじ色でと指定しておりましたが
ランサーさんからのご意見で、エレガント・高級感なら茶系が良いのでは…
とアドバイスいただきました。
確かにそうかもしれません。
私どもは素人ですので、プロの方のアドバイスは大変ありがたいです。

ですので、色はえんじには拘りません。
えんじを含め、他の色でも自由にデザインお願い致します。

どうぞ宜しくお願い致します。
たくさんの良いご提案をありがとうございます。

ご提案を拝見させて頂き、漠然としていたものが
だんだんと具体的にイメージ出来る様になって参りました。

前回、入れて頂きたい文言を挙げさせて頂きましたが
今回訂正し、以下のものを入れて頂きたいと思います。

Beauty&Body School
エステ・アロマテラピー・リフレクソロジー・ボディケア
Beauty&Body Salon
エステ・オイルトリートメント・リフレクソロジー・アロマテラピー
Aroma Shop
エッセンシャルオイル・ナチュラルオイル・ハーブウォーター

カタカナは英語よりも小さめでお願い致します。
字体はお任せいたします。

度々の追記で申し訳ありませんが、どうぞ宜しくお願い致します。

デザインの全体的なイメージが一つに偏らず、エステ・スクール・ショップのそれぞれにリンクしていた事。

縦長の看板がより良く生かされたデザインも気に入りました。

ご提案下さったランサーの皆さま、大変ありがとうございました。

たくさんのご提案に感謝致します。
また、機会がございましたら宜しくお願い致します。

```html
<!DOCTYPE html>
<html lang="ja">
<head>
<meta charset="utf-8">
<title>LUMIA Beauty &amp; Body balance – Sign</title>
<link href="https://fonts.googleapis.com/css2?family=Cormorant+Garamond:ital,wght@0,500;1,500&family=Crimson+Text:wght@400&family=Noto+Serif+JP:wght@500&display=swap" rel="stylesheet">
<style>
  :root {
    --wine: #7a1030;
    --wine-deep: #4f0a1f;
    --wine-light: #b3204f;
    --magenta: #c2305f;
    --amber: #e9a23b;
    --cream: #fbf4ee;
    --white: #ffffff;
    --ink-soft: #f6e6ea;
  }
  html, body {
    margin: 0;
    padding: 0;
    width: 1200px;
    height: 2400px;
    overflow: hidden;
    background: var(--white);
  }
  .sign {
    position: relative;
    width: 1200px;
    height: 2400px;
    overflow: hidden;
    background: var(--wine);
    font-family: "Crimson Text", "Times New Roman", serif;
    color: var(--white);
  }
  .backdrop {
    position: absolute;
    inset: 0;
    width: 1200px;
    height: 2400px;
  }
  .photo {
    position: absolute;
  }
  .photo--facial {
    left: 0; top: 0; width: 1200px; height: 800px;
    clip-path: polygon(500px 0, 1200px 0, 1200px 740px, 980px 700px, 620px 560px, 470px 300px);
    background: radial-gradient(ellipse at 68% 40%, #f8dccb 0%, #eec3a8 45%, #f7ece4 80%, var(--cream) 100%);
  }
  .photo--massage {
    left: 0; top: 880px; width: 900px; height: 820px;
    clip-path: polygon(0 40px, 880px 0, 640px 700px, 0 800px);
    background: linear-gradient(150deg, #3a1a0c 0%, #7a4320 35%, #b8784a 55%, #5a2a12 80%, #2a1006 100%);
  }
  .brand {
    position: absolute;
    left: 84px;
    top: 560px;
    width: 600px;
    text-align: center;
  }
  .brand__name {
    font-family: "Cormorant Garamond", "Times New Roman", serif;
    font-weight: 500;
    font-size: 168px;
    line-height: 1;
    letter-spacing: 6px;
    color: var(--white);
    display: inline-flex;
    align-items: center;
    gap: 20px;
  }
  .brand__dot {
    width: 22px; height: 22px;
    border-radius: 50%;
    background: var(--white);
  }
  .brand__tagline {
    margin-top: 6px;
    font-size: 46px;
    color: var(--white);
    letter-spacing: 1px;
  }
  .services {
    position: absolute;
    right: 50px;
    top: 1315px;
    width: 1000px;
    text-align: right;
  }
  .service { margin-bottom: 72px; }
  .service__title {
    font-size: 80px;
    line-height: 1.05;
    color: var(--white);
  }
  .service__detail {
    font-family: "Noto Serif JP", serif;
    font-weight: 500;
    font-size: 38px;
    line-height: 1.4;
    color: var(--white);
    margin-top: 10px;
  }
  .contact {
    position: absolute;
    left: 0; top: 2170px;
    width: 1200px;
    text-align: center;
  }
  .contact__tel {
    font-family: "Cormorant Garamond", "Times New Roman", serif;
    font-style: italic;
    font-weight: 500;
    font-size: 104px;
    letter-spacing: 8px;
    line-height: 1.1;
  }
  .contact__url {
    font-family: "Cormorant Garamond", "Times New Roman", serif;
    font-size: 56px;
    letter-spacing: 3px;
    margin-top: 4px;
  }
</style>
</head>
<body>
<main class="sign">
  <svg class="backdrop" viewBox="0 0 1200 2400" aria-hidden="true">
    <defs>
      <linearGradient id="satin" x1="0" y1="0" x2="1" y2="1">
        <stop offset="0" stop-color="#8e1438"/>
        <stop offset="0.4" stop-color="#c2305f"/>
        <stop offset="0.7" stop-color="#8a1236"/>
        <stop offset="1" stop-color="#5a0b22"/>
      </linearGradient>
      <linearGradient id="topband" x1="0" y1="0" x2="1" y2="0">
        <stop offset="0" stop-color="#6a0c28"/>
        <stop offset="1" stop-color="#9a1a42"/>
      </linearGradient>
    </defs>
    <rect class="field" width="1200" height="2400" fill="url(#satin)"/>
    <polygon class="band-upper" points="0,430 1200,720 1200,960 0,930" fill="url(#topband)"/>
    <polygon class="paper" points="0,0 1200,0 1200,720 0,440" fill="#fbf4ee"/>
    <polygon class="accent-amber" points="1200,700 1200,960 880,930" fill="#e9a23b"/>
    <polygon class="accent-ribbon" points="700,900 1200,960 1200,1080 820,960" fill="#d24a6e" opacity="0.55"/>
    <polygon class="accent-lower" points="0,1700 640,1580 0,2060" fill="#9c1a3f" opacity="0.7"/>
    <polygon class="accent-lower-edge" points="0,2000 700,1800 0,2140" fill="#c2305f" opacity="0.45"/>
    <rect class="footer-band" y="2140" width="1200" height="260" fill="#4f0a1f"/>
    <line x1="0" y1="2140" x2="1200" y2="2140" stroke="#c2305f" stroke-width="4"/>
  </svg>

  <div class="photo photo--facial" role="img" aria-label="Photo of a woman relaxing with closed eyes and white lily flowers"></div>
  <div class="photo photo--massage" role="img" aria-label="Photo of a woman receiving a back massage with a flower in her hair"></div>

  <div class="brand">
    <div class="brand__name">LUMIA<span class="brand__dot"></span></div>
    <div class="brand__tagline">Beauty &amp; Body balance</div>
  </div>

  <section class="services">
    <div class="service">
      <div class="service__title">Aroma Shop</div>
      <div class="service__detail">◆エステ・アロマテラピー・<br>リフレクソロジー・ボディケア◆</div>
    </div>
    <div class="service">
      <div class="service__title">Beauty &amp; Body Salon</div>
      <div class="service__detail">◆エステ・オイルトリートメント・<br>リフレクソロジー・アロマテラピー◆</div>
    </div>
    <div class="service">
      <div class="service__title">Beauty &amp; Body School</div>
      <div class="service__detail">◆エッセンシャルオイル・ナチュラルオイル・ハーブウォーター◆</div>
    </div>
  </section>

  <footer class="contact">
    <div class="contact__tel">Tel 233-444-7777</div>
    <div class="contact__url">http://www.lumia-beauty.jp</div>
  </footer>
</main>
</body>
</html>
```